Antigen Preservation Bureau

The company will provide a contract research services to stabilize various viruses, viral vectors, and vaccines. It may offer some licensing opportunities for stabilizing technologies. Main area of applications are pharmaceutical, therapeutic, and vaccination field. The company aspires to develop room temperature vaccines for global distribution beyond the current cold chain.

Target Market(s)

pharmaceutical, therapeutic and vaccination fields

Coding

Coded - Design and coding required

Number of Pages Required

4 page

Requirements
Must have
• Incorporate a APB logo, attached at the bottom, on the Web page

```html
<!DOCTYPE html>
<html lang="en">
<head>
<meta charset="utf-8">
<title>Antigen Preservation Bureau</title>
<link href="https://fonts.googleapis.com/css2?family=Raleway:wght@400;500;600&family=Open+Sans:wght@400;600&display=swap" rel="stylesheet">
<style>
:root{
  --green:#4f9a78;
  --green-dark:#3f8667;
  --gold:#c79a3c;
  --grey-tag:#7d8a86;
  --ink:#3a3a3a;
  --muted:#8a8a8a;
  --light:#f3f3f3;
  --white:#ffffff;
}
*{margin:0;padding:0;box-sizing:border-box}
html,body{width:1200px;height:2712px;overflow:hidden}
body{background:var(--white);font-family:"Open Sans",Arial,sans-serif;color:var(--ink);position:relative}
.wrap{position:absolute;left:0;width:1200px}
h2{font-family:"Raleway",Arial,sans-serif;font-weight:500;font-size:38px;letter-spacing:1px;text-align:center;color:var(--ink)}
.rule{width:90px;height:3px;background:var(--gold);margin:14px auto 0}
.lead{font-size:13px;color:var(--muted);text-align:center;margin-top:28px}
.btn{display:inline-block;background:var(--green);color:var(--white);font-family:"Raleway",Arial,sans-serif;font-weight:600;font-size:15px;letter-spacing:1px;padding:14px 32px;border-radius:26px}

/* header */
.site-header{top:0;height:120px;border-top:6px solid var(--green);background:var(--white);display:flex;align-items:center;justify-content:space-between;padding:0 40px 0 40px}
.brand{display:flex;align-items:center;gap:14px}
.brand-dot{width:56px;height:56px;border-radius:50%;background:var(--green)}
.brand-name{font-family:"Raleway",Arial,sans-serif;font-weight:600;font-size:19px;line-height:1.15;color:var(--green);text-transform:uppercase;letter-spacing:1px;width:230px}
.nav{display:flex;align-items:center;gap:44px;font-family:"Raleway",Arial,sans-serif;font-size:14px;font-weight:600;color:var(--ink)}
.nav .active{color:var(--green)}
.search{width:50px;height:50px;border:2px solid #cfcfcf;border-radius:50%;display:flex;align-items:center;justify-content:center}

/* hero */
.hero{top:120px;height:520px;background:linear-gradient(90deg,#eef5f3 0%,#dfeeea 35%,#9fc8c4 60%,#7fa9b2 80%,#c9dbe0 100%)}
.hero-text{position:absolute;left:110px;top:120px;width:440px;text-align:center}
.hero-title{font-family:"Raleway",Arial,sans-serif;font-weight:600;font-size:64px;color:var(--green);letter-spacing:2px;line-height:1}
.hero-sub{font-family:"Raleway",Arial,sans-serif;font-weight:500;font-size:30px;letter-spacing:1px;margin-top:10px;color:var(--ink)}
.hero-copy{font-size:12px;color:#555;margin-top:18px;line-height:1.6}
.hero-text .btn{margin-top:30px}

/* applications */
.apps{top:640px;height:540px;padding-top:56px}
.app-row{display:flex;justify-content:center;gap:80px;margin-top:46px}
.app{width:280px;text-align:center}
.app-icon{width:190px;height:190px;border-radius:50%;margin:0 auto;border:10px solid #f0f0f0}
.app-icon.green{background:radial-gradient(circle,#5fa487 45%,#d9e9e1 46%)}
.app-icon.gold{background:radial-gradient(circle,#c99a3c 45%,#efe3c8 46%)}
.app-icon.grey{background:radial-gradient(circle,#7a7f7d 45%,#e2e4e3 46%)}
.app h3{font-family:"Raleway",Arial,sans-serif;font-weight:600;font-size:18px;letter-spacing:1px;margin-top:20px}
.app h3.green{color:var(--green)}.app h3.gold{color:var(--gold)}.app h3.grey{color:#6e7472}
.app p{font-size:12px;color:var(--muted);line-height:1.7;margin-top:10px}

/* about */
.about{top:1180px;height:380px}
.about-photo{position:absolute;left:0;top:0;width:820px;height:380px;background:linear-gradient(135deg,#dfe9ee 0%,#9fb8c6 40%,#6c8ea3 75%,#b5c8d2 100%)}
.about-card{position:absolute;left:780px;top:20px;width:420px;height:340px;background:var(--white);border-left:5px solid var(--green);padding:40px 36px}
.about-card h2{text-align:left;font-size:40px}
.about-card .rule{margin:12px 0 0}
.about-card p{font-size:12px;color:var(--muted);line-height:1.8;margin-top:22px}
.about-card .btn{position:absolute;right:36px;bottom:30px;font-size:13px;padding:12px 26px}

/* services */
.services{top:1560px;height:480px;padding-top:60px}
.service-row{display:flex;justify-content:center;gap:14px;margin-top:36px}
.service{width:318px;height:292px;position:relative}
.service-media{height:244px}
.service-media.viruses{background:radial-gradient(circle at 50% 45%,#e04a78 0%,#a0214d 45%,#3b0b1e 100%)}
.service-media.vectors{background:radial-gradient(circle at 55% 50%,#6fb4e6 0%,#2c6fb8 45%,#0f2a5a 100%)}
.service-media.vaccines{background:linear-gradient(135deg,#7da7c7 0%,#c8dbe8 45%,#5e7f9c 100%)}
.service-tag{height:48px;display:flex;align-items:center;justify-content:space-between;padding:0 18px;color:var(--white);font-family:"Raleway",Arial,sans-serif;font-weight:600;font-size:14px;letter-spacing:1px}
.tag-green{background:var(--green)}.tag-grey{background:var(--grey-tag)}.tag-gold{background:var(--gold)}
.plus{width:20px;height:20px;border-radius:50%;background:rgba(255,255,255,.85);display:flex;align-items:center;justify-content:center;color:var(--ink);font-size:15px;line-height:1}

/* testimonial */
.testimonial{top:2080px;height:290px;background:var(--light)}
.quote{position:absolute;left:190px;top:50px;width:600px}
.quote-mark{font-family:Georgia,serif;font-size:40px;color:#b8b8b8;line-height:1;position:absolute;left:-36px;top:-6px}
.quote p{font-size:12px;color:#666;line-height:1.8}
.quote .who{margin-top:18px;font-family:"Raleway",Arial,sans-serif;font-weight:600;font-size:12px;color:var(--ink);letter-spacing:1px}
.quote .when{font-size:11px;color:var(--muted);margin-top:2px}
.portrait{position:absolute;left:800px;top:55px;width:180px;height:180px;border-radius:50%;border:6px solid var(--white);background:linear-gradient(160deg,#b08870 0%,#7a4e3a 55%,#e8d6c8 100%)}

/* footer */
.site-footer{top:2392px;height:320px;background:var(--green);color:var(--white)}
.social{display:flex;justify-content:center;gap:26px;padding-top:34px}
.social span{width:50px;height:50px;border:2px solid rgba(255,255,255,.75);border-radius:50%}
.footer-rule{width:1080px;height:1px;background:rgba(255,255,255,.35);margin:30px auto 0}
.contact-row{display:flex;justify-content:space-between;width:1000px;margin:34px auto 0}
.contact{display:flex;gap:14px;align-items:flex-start}
.contact-icon{width:44px;height:44px;border:2px solid rgba(255,255,255,.8);border-radius:50%;display:flex;align-items:center;justify-content:center;flex:none}
.contact h4{font-family:"Raleway",Arial,sans-serif;font-weight:600;font-size:17px}
.contact p{font-size:11px;line-height:1.6;opacity:.9;margin-top:2px}
.copyright{text-align:center;font-size:11px;margin-top:46px;opacity:.9}
</style>
</head>
<body>

<header class="wrap site-header">
  <div class="brand">
    <span class="brand-dot"></span>
    <span class="brand-name">Antigen Preservation Bureau</span>
  </div>
  <nav class="nav">
    <span class="active">HOME</span><span>ABOUT US</span><span>SERVICES</span><span>NEWS</span><span>CONTACT US</span>
    <span class="search"><svg width="20" height="20" viewBox="0 0 20 20"><circle cx="8" cy="8" r="6" fill="none" stroke="#555" stroke-width="2"/><line x1="12.5" y1="12.5" x2="18" y2="18" stroke="#555" stroke-width="2"/></svg></span>
  </nav>
</header>

<section class="wrap hero" role="img" aria-label="Scientist in safety glasses and gloves working at a laboratory bench">
  <div class="hero-text">
    <div class="hero-title">ANTIGEN</div>
    <div class="hero-sub">PRESERVATION BUREAU</div>
    <p class="hero-copy">We stabilize viruses, viral vectors and vaccines so that they stay potent at room temperature, from the lab bench to the field.</p>
    <span class="btn">READ MORE</span>
  </div>
</section>

<section class="wrap apps">
  <h2>AREA OF APPLICATIONS</h2>
  <div class="rule"></div>
  <p class="lead">Our stabilizing technologies serve three fields, each with its own needs for storage and transport.</p>
  <div class="app-row">
    <div class="app">
      <div class="app-icon green" role="img" aria-label="Pharmaceutical bottle icon"></div>
      <h3 class="green">PHARMACEUTICAL</h3>
      <p>Longer shelf life for biologic products, fewer losses in storage and simpler handling for partners worldwide.</p>
    </div>
    <div class="app">
      <div class="app-icon gold" role="img" aria-label="Therapeutic capsule icon"></div>
      <h3 class="gold">THERAPEUTIC</h3>
      <p>Stable viral vectors for gene and cell therapy, keeping activity high from production to the patient.</p>
    </div>
    <div class="app">
      <div class="app-icon grey" role="img" aria-label="Vaccination syringe icon"></div>
      <h3 class="grey">VACCINATION</h3>
      <p>Room temperature vaccines for global distribution, reaching communities beyond the current cold chain.</p>
    </div>
  </div>
</section>

<section class="wrap about">
  <div class="about-photo" role="img" aria-label="Researchers in protective suits working in a clean room laboratory"></div>
  <div class="about-card">
    <h2>ABOUT US</h2>
    <div class="rule"></div>
    <p>We are a contract research group focused on the stability of viruses, vectors and vaccines. Our team develops formulations that hold potency without refrigeration and offers licensing of proven stabilizing technologies to industry partners.</p>
    <span class="btn">READ MORE</span>
  </div>
</section>

<section class="wrap services">
  <h2>OUR SERVICES</h2>
  <div class="rule"></div>
  <p class="lead">Contract research and licensing across the full range of live and inactivated biological materials.</p>
  <div class="service-row">
    <div class="service">
      <div class="service-media viruses" role="img" aria-label="Magnified virus particles"></div>
      <div class="service-tag tag-green"><span>VIRUSES</span><span class="plus">+</span></div>
    </div>
    <div class="service">
      <div class="service-media vectors" role="img" aria-label="Viral vector particle illustration"></div>
      <div class="service-tag tag-grey"><span>VIRAL VECTORS</span><span class="plus">+</span></div>
    </div>
    <div class="service">
      <div class="service-media vaccines" role="img" aria-label="Vaccine vial and syringe"></div>
      <div class="service-tag tag-gold"><span>VACCINES</span><span class="plus">+</span></div>
    </div>
  </div>
</section>

<section class="wrap testimonial">
  <div class="quote">
    <span class="quote-mark">&ldquo;</span>
    <p>Working with the team changed how we plan distribution. Our vector batches now stay stable for weeks outside the freezer, and the data package they delivered was clear, complete and ready for review. We have already started a second project with them and expect a long partnership that brings our programs to many more regions.</p>
    <div class="who">NORA HALVORSEN</div>
    <div class="when">Posted on 12 Jan 2024</div>
  </div>
  <div class="portrait" role="img" aria-label="Portrait photo of the client giving the testimonial"></div>
</section>

<footer class="wrap site-footer">
  <div class="social"><span></span><span></span><span></span><span></span><span></span><span></span></div>
  <div class="footer-rule"></div>
  <div class="contact-row">
    <div class="contact">
      <span class="contact-icon"><svg width="18" height="22" viewBox="0 0 18 22"><path d="M9 1a7 7 0 0 0-7 7c0 5 7 13 7 13s7-8 7-13a7 7 0 0 0-7-7z" fill="none" stroke="#fff" stroke-width="2"/><circle cx="9" cy="8" r="2.5" fill="#fff"/></svg></span>
      <div><h4>Address -</h4><p>18 Harbor Lane, Suite 4<br>Westbrook Park</p></div>
    </div>
    <div class="contact">
      <span class="contact-icon"><svg width="22" height="16" viewBox="0 0 22 16"><rect x="1" y="1" width="20" height="14" fill="none" stroke="#fff" stroke-width="2"/><path d="M1 1l10 8 10-8" fill="none" stroke="#fff" stroke-width="2"/></svg></span>
      <div><h4>Email</h4><p>info@antigen-preservation.org</p></div>
    </div>
    <div class="contact">
      <span class="contact-icon"><svg width="20" height="20" viewBox="0 0 20 20"><path d="M4 1l4 4-2 3c1 3 3 5 6 6l3-2 4 4-3 3C8 19 1 12 1 4z" fill="none" stroke="#fff" stroke-width="2"/></svg></span>
      <div><h4>Phone</h4><p>Mobile - (000) 123 4567</p></div>
    </div>
  </div>
  <p class="copyright">&copy; Copyright 2024 Antigen Preservation Bureau. All rights reserved.</p>
</footer>

</body>
</html>
```